Get me out of Jail business cards!!!!

I need business cards done for my business. I own a BailBonds and I get people out of jail!

Colors are red white and black

I need it to say on the card these details:

Freedom Hop Bailbonds

427 S Calloway St
Pinewick, FL 30517

555-310-0187

Open 24/7

On the back of the card:

Must check in every Tuesday.

______/______/______ court date
____________________ time
You must know your court date at all times!

Marla Whitcombe - owner
Jolene Whitcombe - agent
Rosalind Pickett - agent

Industry/Entity Type

Bail bonds

Contact Information for Business Card

Colors are red white and black I need it to say on the card these details: Freedom Hop Bailbonds 427 S Calloway St Pinewick, FL 30517 555-310-0187 Open 24/7 On the back of the card: Must check in every Tuesday. ______/______/______ court date ____________________ time You must know your court date at all times! Marla Whitcombe - owner Jolene Whitcombe - agent Rosalind Pickett - agent

Font styles to use
Serif
Sans Serif

Colors
EB3D1F
EC4F4E
F09395
F8D3D4
FCEDEE

Requirements
Must have
• I listed the must haves in the business card details
Nice to have
• Handcuffs or jail bars or a man in a black and white suit

```html
<!DOCTYPE html>
<html lang="en">
<head>
<meta charset="utf-8">
<title>Freedom Hop Bailbonds – Business Card</title>
<link rel="stylesheet" href="https://fonts.googleapis.com/css2?family=Arimo&family=Montserrat:ital,wght@0,500;0,700;1,400;1,700&display=swap">
<style>
  :root {
    --paper: #ffffff;
    --card: #000000;
    --bar: #1c1c1c;
    --ink: #ffffff;
    --accent: #ff0000;
    --cuffs: #1a1a1a;
  }
  * { margin: 0; padding: 0; box-sizing: border-box; }
  html, body {
    width: 1200px; height: 1200px; overflow: hidden;
    background: var(--paper);
  }
  .canvas { position: relative; width: 1200px; height: 1200px; }
  .card {
    position: absolute; left: 211px; width: 685px; height: 370px;
    background: var(--card); overflow: hidden;
    font-family: "Montserrat", sans-serif; color: var(--ink);
  }
  .card--front { top: 198px; }
  .card--back { top: 681px; }

  .bar { position: absolute; width: 15px; background: var(--bar); }
  .bar--top { top: 0; height: 152px; }
  .bar--bottom { top: 223px; height: 147px; }

  .brand-name {
    position: absolute; left: 19px; top: 152px; width: 300px; height: 71px;
    display: flex; align-items: center; justify-content: center;
    font-weight: 500; font-size: 22px; color: var(--ink); white-space: nowrap;
  }
  .divider {
    position: absolute; left: 376px; top: 61px; width: 3px; height: 247px;
    background: var(--ink);
  }
  .contact { position: absolute; right: 37px; text-align: right; white-space: nowrap; line-height: 1.2; }
  .contact__name { top: 82px; font-weight: 700; font-size: 22.5px; }
  .contact__role { top: 105px; font-style: italic; font-size: 15px; color: var(--accent); }
  .contact__address { top: 175px; font-weight: 500; font-size: 17.5px; line-height: 19px; }
  .contact__phone { top: 233px; font-weight: 500; font-size: 17.5px; }
  .contact__hours { top: 272px; font-weight: 700; font-size: 18px; color: var(--accent); }

  .checkin {
    position: absolute; left: 0; width: 100%; top: 59px; text-align: center;
    font-style: italic; font-size: 21px;
  }
  .cuffs-art {
    position: absolute; left: 160px; top: 101px; width: 365px; height: 200px;
    border-radius: 100px; background: var(--cuffs);
  }
  .form-line {
    position: absolute; font-family: "Arimo", sans-serif; font-size: 20.5px;
    white-space: nowrap;
  }
  .form-line--date { left: 182px; top: 154px; }
  .form-line--time { left: 203px; top: 177px; }
  .blank {
    display: inline-block; height: 19px; border-bottom: 1.5px solid var(--ink);
    vertical-align: baseline;
  }
  .reminder {
    position: absolute; left: 0; width: 100%; top: 330px; text-align: center;
    font-style: italic; font-weight: 700; font-size: 13.5px; color: var(--accent);
  }
</style>
</head>
<body>
<div class="canvas">
  <section class="card card--front">
    <div class="bar bar--top" style="left:19px"></div>
    <div class="bar bar--top" style="left:58px"></div>
    <div class="bar bar--top" style="left:97px"></div>
    <div class="bar bar--top" style="left:135px"></div>
    <div class="bar bar--top" style="left:174px"></div>
    <div class="bar bar--top" style="left:213px"></div>
    <div class="bar bar--top" style="left:252px"></div>
    <div class="bar bar--top" style="left:290px"></div>
    <div class="bar bar--bottom" style="left:19px"></div>
    <div class="bar bar--bottom" style="left:58px"></div>
    <div class="bar bar--bottom" style="left:97px"></div>
    <div class="bar bar--bottom" style="left:135px"></div>
    <div class="bar bar--bottom" style="left:174px"></div>
    <div class="bar bar--bottom" style="left:213px"></div>
    <div class="bar bar--bottom" style="left:252px"></div>
    <div class="bar bar--bottom" style="left:290px"></div>
    <div class="brand-name">Freedom Hop Bailbonds</div>
    <div class="divider"></div>
    <div class="contact contact__name">Marla Whitcombe</div>
    <div class="contact contact__role">owner</div>
    <div class="contact contact__address">427 S Calloway St<br>Pinewick, FL 30517</div>
    <div class="contact contact__phone">555-310-0187</div>
    <div class="contact contact__hours">Open 24/7</div>
  </section>

  <section class="card card--back">
    <p class="checkin">Must check in every Tuesday.</p>
    <div class="cuffs-art" role="img" aria-label="Faint handcuffs illustration"></div>
    <p class="form-line form-line--date"><span class="blank" style="width:71px"></span>/<span class="blank" style="width:71px"></span>/<span class="blank" style="width:71px"></span> court date</p>
    <p class="form-line form-line--time"><span class="blank" style="width:235px"></span> time</p>
    <p class="reminder">You must know your court date at all times!</p>
  </section>
</div>
</body>
</html>
```